Trondel Group letterhead

Hi,

I need a letterhead template created for our business. This should be done in word format and A4 size. The images need to not move in the template ie when I am adding writing in etc. and should flow on when I get to a second page.

I have attached our logo templates below.

Other details to include on the letterhead somewhere are:

0438 571 962
Max@Trondelelectrical.example.com.au
PO Box 781 Marrowdale NSW 2163
ABN: 57 318 492 076

Thanks!

```html
<!DOCTYPE html>
<html lang="en">
<head>
<meta charset="utf-8">
<title>Trondel Group Letterhead</title>
<link rel="stylesheet" href="https://fonts.googleapis.com/css2?family=Open+Sans:wght@400;500&family=Lato:wght@400;700&family=Manrope:wght@500&display=swap">
<style>
  :root {
    --orange: #f25100;
    --ink: #2d2d2d;
    --body: #7a7a7a;
    --rule: #6e6e6e;
    --sig-tone: #e9e9e9;
    --paper: #ffffff;
  }
  * { margin: 0; padding: 0; box-sizing: border-box; }
  html, body { width: 999px; height: 1200px; overflow: hidden; background: var(--paper); }
  .letterhead { position: relative; width: 999px; height: 1200px; background: var(--paper); font-family: "Open Sans", sans-serif; }

  .brand { position: absolute; left: 78px; top: 78px; display: flex; align-items: center; gap: 12px; }
  .brand-dot { width: 46px; height: 46px; border-radius: 50%; border: 5px solid var(--ink); }
  .brand-name { font-family: "Open Sans", sans-serif; font-weight: 500; font-size: 28px; color: var(--ink); letter-spacing: 0.5px; }

  .company-contacts { position: absolute; left: 682px; top: 60px; font-family: "Lato", sans-serif; font-size: 13.5px; color: var(--ink); list-style: none; }
  .company-contacts li { display: flex; align-items: center; gap: 6px; height: 25px; }
  .company-contacts svg { width: 16px; height: 16px; flex: none; }
  .company-contacts .abn { margin-top: 3px; }
  .abn-label { color: var(--orange); }

  .header-rule { position: absolute; left: 70px; top: 185px; width: 857px; height: 1px; background: var(--rule); }

  .recipient { position: absolute; left: 88px; top: 244px; }
  .recipient-name { font-size: 26px; font-weight: 400; color: var(--orange); line-height: 32px; }
  .recipient-role { font-family: "Lato", sans-serif; font-size: 13.5px; color: var(--ink); margin-top: 2px; }
  .recipient-details { list-style: none; margin-top: 14px; font-size: 16px; color: var(--body); }
  .recipient-details li { height: 24px; line-height: 24px; }
  .recipient-details b { display: inline-block; width: 34px; color: var(--orange); font-weight: 500; }

  .letter-date { position: absolute; right: 92px; top: 378px; font-size: 16px; color: var(--body); }

  .letter-body { position: absolute; left: 90px; top: 454px; width: 818px; font-size: 16.5px; line-height: 22.5px; color: var(--body); text-align: justify; }
  .letter-body p + p { margin-top: 22px; }

  .signature { position: absolute; left: 108px; top: 816px; width: 145px; height: 78px; background: var(--sig-tone); border-radius: 4px; }
  .signatory { position: absolute; left: 90px; top: 897px; font-family: "Manrope", sans-serif; font-weight: 500; font-size: 23px; color: var(--ink); }

  .footer-band { position: absolute; bottom: 0; height: 17px; }
  .footer-band.accent { left: 0; width: 556px; background: var(--orange); }
  .footer-band.dark { right: 0; width: 139px; background: var(--ink); }
</style>
</head>
<body>
<main class="letterhead">
  <div class="brand">
    <span class="brand-dot"></span>
    <span class="brand-name">Trondel Group</span>
  </div>

  <ul class="company-contacts">
    <li>
      <svg viewBox="0 0 16 16"><rect width="16" height="16" rx="3" fill="#f25100"/><path d="M5 3.5l2 2.2-1 1.2c.6 1.3 1.7 2.4 3 3l1.2-1 2.2 2-1 1.6c-3.6-.3-6.8-3.5-7.1-7.1z" fill="#fff"/></svg>
      0438 571 962
    </li>
    <li>
      <svg viewBox="0 0 16 16"><rect width="16" height="16" rx="3" fill="#f25100"/><rect x="3" y="4.5" width="10" height="7" fill="none" stroke="#fff" stroke-width="1.2"/><path d="M3 4.5l5 4 5-4" fill="none" stroke="#fff" stroke-width="1.2"/></svg>
      Max@Trondelelectrical.example.com.au
    </li>
    <li>
      <svg viewBox="0 0 16 16"><rect width="16" height="16" rx="3" fill="#f25100"/><path d="M8 13.5s-3.8-4-3.8-6.6a3.8 3.8 0 0 1 7.6 0c0 2.6-3.8 6.6-3.8 6.6z" fill="#fff"/><circle cx="8" cy="6.9" r="1.4" fill="#f25100"/></svg>
      PO Box 781 Marrowdale NSW 2163
    </li>
    <li class="abn"><span class="abn-label">ABN:</span>&nbsp;57 318 492 076</li>
  </ul>

  <div class="header-rule"></div>

  <section class="recipient">
    <h2 class="recipient-name">James Doe</h2>
    <p class="recipient-role">Chief Director</p>
    <ul class="recipient-details">
      <li><b>A :</b>4986 Northwest Avenue, Carverton 20025</li>
      <li><b>W :</b>www.companywebsite.example.com</li>
      <li><b>P :</b>+00 123 456 78</li>
      <li><b>M :</b>companyname@mailbox.example.com</li>
    </ul>
  </section>

  <p class="letter-date">12 December, 2024</p>

  <article class="letter-body">
    <p>Lorem ipsum dolor sit amet, consectetuer adipiscing elit, sed diam nonummy nibh euismod tincidunt ut laoreet dolore magna aliquam erat volutpat. Ut wisi enim ad minim veniam, quis nostrud exerci tation ullamcorper suscipit lobortis nisl ut aliquip ex ea commodo consequat. Duis autem vel eum iriure dolor in hendrerit in vulputate velit esse molestie consequat, vel illum dolore eu feugiat nulla facilisis at vero eros et accumsan et iusto odio dignissim qui blandit praesent luptatum zzril delenit augue duis dolore te feugait nulla facilisi.</p>
    <p>Lorem ipsum dolor sit amet, cons ectetuer adipiscing elit, sed diam nonummy nibh euismod tincidunt ut laoreet dolore magna aliquam erat volutpat. Ut wisi enim ad minim veniam, quis nostrud exerci tation ullamcorper suscipit lobortis nisl ut aliquip ex ea commodo consequat.</p>
    <p>Lorem ipsum dolor sit amet, consectetuer adipiscing elit, sed diam nonummy nibh euismod tincidunt ut laoreet dolore magna aliquam eratveniam, quis nostrud exerci tation ullamcorper suscipit lobortis nisl ut aliquip ex ea commodo consequat. Lorem ipsum dolor sit zamet, consectetuer adipiscing elit, sed diam nonummy nibh euismod tincidunt.</p>
  </article>

  <div class="signature" role="img" aria-label="Handwritten signature"></div>
  <p class="signatory">Mr. Jone Smith</p>

  <div class="footer-band accent"></div>
  <div class="footer-band dark"></div>
</main>
</body>
</html>
```